Post Card Invitation to Wedding Rehearsal Dinner and After Party

This post card should serve as invitations for two events in the wedding weekend for two San Francisco grooms, Derek and Leon.
Each side of the card should have distinct looks and information but tied together with “Before” on the front and “After” on the back.
POST CARD FRONT
Required text:
BEFORE
Derek and Leon’s Wedding: Rehearsal Dinner
Friday, May 22, 2015
5:30 PM
Larkfield Kitchen Yard
615 Fenwick Street @ Marlow
San Francisco, CA
Please also convey the following information without necessarily quoting directly: This rehearsal dinner will be held in a private enclosed space in the food truck park. We we will serve beer and wine in our space and provide tickets to purchase food from any of the trucks in the park. Dress is casual.
Look and feel of the card should have a modern, “hipster” feel to it. If you search Google images for “Hipster design” or “hipster infographic” you should get a sense of the overall design and colors. The website for the venue is http://larkfieldkitchenyard.com/ for reference but please DO NOT use any images or logos from the site.
----------------------
POST CARD REVERSE
Required Text:
AFTER
Derek and Leon’s Wedding: After Party
Saturday, May 23, 2015
7:30 PM
Harbor Crest Sailing Club
47 Pelling Road
San Francisco, CA
Please also convey the following information without necessarily quoting directly: Black-tie optional. Dancing, snacks and dessert and cocktails with panoramic views of the San Francisco Bay and Golden Gate Bridge.
This should have a much different look and feel from the front of the card. It should convey an elegant black-tie affair. If you search Google images for “black tie after party invitation” you should get some examples of an overall feel that I am aiming for. The website for the venue is www.hcsailclub.com but DO NOT use any of the images or logos from the site.
Industry/Entity Type
Wedding
Look and feel
Each slider illustrates characteristics of the customer's brand and the style your logo design should communicate.

```html
<!DOCTYPE html>
<html lang="en">
<head>
<meta charset="utf-8">
<title>Derek &amp; Leon – Before &amp; After Invitations</title>
<link href="https://fonts.googleapis.com/css2?family=Didact+Gothic&family=Pacifico&family=Poiret+One&family=Archivo+Black&family=Architects+Daughter&family=Great+Vibes&family=Cormorant+Garamond:wght@400&display=swap" rel="stylesheet">
<style>
  :root {
    --backdrop: #e9e6e1;
    --paper: #ffffff;
    --ink: #111111;
    --night: #0b0b0b;
    --pearl: #f4f4f4;
    --silver: #b9b9b9;
    --ornament-tone: linear-gradient(90deg, #3a3a3a, #9a9a9a 50%, #3a3a3a);
  }
  * { box-sizing: border-box; margin: 0; padding: 0; }
  html, body { width: 1200px; height: 1000px; overflow: hidden; }
  body { background: var(--backdrop); position: relative; }

  .card {
    position: absolute; top: 160px; width: 480px; height: 680px;
    box-shadow: 0 6px 18px rgba(0,0,0,.18);
  }
  .card--before { left: 90px; background: var(--paper); color: var(--ink); }
  .card--after { left: 630px; background: var(--night); color: var(--pearl); }
  .abs { position: absolute; }
  .centered { left: 0; right: 0; text-align: center; }

  /* BEFORE side */
  .emblem { left: 0; top: 0; }
  .emblem__text { font-family: 'Didact Gothic', sans-serif; fill: var(--ink); }
  .before-word {
    top: 168px; left: 150px; font-family: 'Pacifico', cursive;
    font-size: 48px; line-height: 1; font-weight: 700;
  }
  .event-line {
    top: 215px; font-family: 'Didact Gothic', sans-serif; font-size: 17.5px;
  }
  .date-row { top: 250px; left: 22px; right: 22px; height: 76px; }
  .date-row__day {
    position: absolute; left: 0; top: 0; font-family: 'Poiret One', cursive;
    font-size: 58px; line-height: 1;
  }
  .date-row__badge { position: absolute; left: 168px; top: 4px; }
  .date-row__suffix {
    position: absolute; left: 244px; top: 8px; font-family: 'Archivo Black', sans-serif; font-size: 18px;
  }
  .date-row__of {
    position: absolute; left: 250px; top: 30px; font-family: 'Didact Gothic', sans-serif; font-size: 15px;
  }
  .date-row__month {
    position: absolute; left: 282px; top: 6px; font-family: 'Archivo Black', sans-serif;
    font-size: 46px; line-height: 1; letter-spacing: 1px;
  }
  .rule-double { top: 334px; left: 18px; right: 18px; height: 8px; border-top: 2px solid var(--ink); border-bottom: 2px solid var(--ink); }
  .time {
    top: 410px; left: 22px; font-family: 'Poiret One', cursive; font-size: 46px; line-height: 1; font-weight: 400;
  }
  .crossed-arrows { top: 372px; left: 196px; }
  .venue {
    top: 390px; left: 300px; width: 170px; font-family: 'Architects Daughter', cursive;
    font-size: 25px; line-height: 1.05;
  }
  .address { top: 498px; font-family: 'Didact Gothic', sans-serif; font-size: 16px; line-height: 1.3; }
  .crown { top: 558px; width: 96px; height: 62px; background: var(--ink); border-radius: 6px 6px 2px 2px; }
  .crown--left { left: 42px; }
  .crown--right { right: 42px; width: 84px; height: 50px; top: 566px; border-radius: 40px 40px 4px 4px; }

  /* AFTER side */
  .ornament { background: var(--ornament-tone); opacity: .85; }
  .ornament--border-top { top: 0; left: 0; right: 0; height: 46px; }
  .ornament--border-bottom { bottom: 0; left: 0; right: 0; height: 70px; }
  .ornament--crest { left: 200px; width: 80px; height: 26px; border-radius: 12px; }
  .ornament--crest-top { top: 68px; }
  .ornament--crest-bottom { top: 178px; }
  .ornament--divider { top: 352px; left: 150px; width: 180px; height: 12px; border-radius: 6px; }
  .hairline { left: 70px; right: 70px; height: 2px; background: var(--pearl); }
  .hairline--top { top: 102px; }
  .hairline--bottom { top: 170px; }
  .couple { top: 108px; font-family: 'Great Vibes', cursive; font-size: 50px; line-height: 1.1; }
  .after-word { top: 228px; font-family: 'Cormorant Garamond', serif; font-size: 36px; }
  .after-line { top: 290px; font-family: 'Great Vibes', cursive; font-size: 27px; }
  .details {
    top: 392px; font-family: 'Didact Gothic', sans-serif; font-size: 21px; line-height: 1.28; color: var(--silver);
  }
</style>
</head>
<body>

<section class="card card--before" aria-label="Rehearsal dinner invitation">
  <svg class="abs emblem" width="480" height="170" viewBox="0 0 480 170" aria-hidden="true">
    <g stroke="var(--ink)" stroke-width="2.5" fill="none">
      <line x1="230" y1="12" x2="230" y2="32"/>
      <line x1="230" y1="142" x2="230" y2="164"/>
      <line x1="150" y1="28" x2="162" y2="44"/>
      <line x1="310" y1="28" x2="298" y2="44"/>
      <line x1="150" y1="146" x2="162" y2="130"/>
      <line x1="310" y1="146" x2="298" y2="130"/>
      <polygon points="105,88 230,40 355,88 230,136"/>
      <polygon points="117,88 230,47 343,88 230,129" stroke-width="1.5"/>
      <line x1="30" y1="130" x2="108" y2="130"/>
      <line x1="360" y1="58" x2="440" y2="58"/>
    </g>
    <g fill="var(--ink)">
      <polygon points="108,124 122,130 108,136"/>
      <polygon points="440,52 454,58 440,64"/>
      <polygon points="30,130 22,122 28,122 36,130 28,138 22,138"/>
      <polygon points="368,58 360,50 366,50 374,58 366,66 360,66"/>
    </g>
    <text class="emblem__text" x="230" y="72" text-anchor="middle" font-size="14">05</text>
    <text class="emblem__text" x="230" y="98" text-anchor="middle" font-size="26">DEREK &amp; LEON</text>
    <text class="emblem__text" x="230" y="120" text-anchor="middle" font-size="14">22</text>
  </svg>

  <svg class="abs" style="left:0;top:160px" width="480" height="60" viewBox="0 0 480 60" aria-hidden="true">
    <g stroke="var(--ink)" stroke-width="2.5">
      <line x1="302" y1="12" x2="450" y2="12"/>
      <line x1="22" y1="45" x2="140" y2="45"/>
    </g>
    <g fill="var(--ink)">
      <polygon points="302,6 288,12 302,18"/>
      <polygon points="450,12 458,4 452,4 444,12 452,20 458,20"/>
      <polygon points="140,39 154,45 140,51"/>
      <polygon points="22,45 14,37 20,37 28,45 20,53 14,53"/>
    </g>
  </svg>
  <p class="abs before-word">before</p>
  <p class="abs centered event-line">Derek and Leon’s Wedding: Rehearsal Dinner</p>

  <div class="abs date-row">
    <span class="date-row__day">friday</span>
    <svg class="date-row__badge" width="72" height="62" viewBox="0 0 72 62" aria-hidden="true">
      <polygon points="18,3 54,3 70,31 54,59 18,59 2,31" fill="none" stroke="var(--ink)" stroke-width="2.5"/>
      <circle cx="36" cy="31" r="22" fill="none" stroke="var(--ink)" stroke-width="2"/>
      <text x="36" y="42" text-anchor="middle" font-family="Archivo Black, sans-serif" font-size="30" fill="var(--ink)">22</text>
    </svg>
    <span class="date-row__suffix">ND</span>
    <span class="date-row__of">of</span>
    <span class="date-row__month">MAY</span>
  </div>
  <div class="abs rule-double"></div>

  <p class="abs time">5:30 PM</p>
  <svg class="abs crossed-arrows" width="90" height="110" viewBox="0 0 90 110" aria-hidden="true">
    <g stroke="var(--ink)" stroke-width="2.5" fill="none">
      <line x1="10" y1="10" x2="80" y2="100"/>
      <line x1="80" y1="10" x2="10" y2="100"/>
      <circle cx="45" cy="55" r="6"/>
    </g>
    <g fill="var(--ink)">
      <polygon points="4,2 18,6 8,16"/>
      <polygon points="86,2 72,6 82,16"/>
    </g>
  </svg>
  <p class="abs venue">Larkfield Kitchen Yard</p>
  <p class="abs centered address">615 Fenwick Street @ Marlow<br>San Francisco, CA</p>

  <div class="abs crown crown--left" role="img" aria-label="Illustrated spiked crown icon"></div>
  <div class="abs crown crown--right" role="img" aria-label="Illustrated rounded crown icon"></div>
</section>

<section class="card card--after" aria-label="After party invitation">
  <div class="abs ornament ornament--border-top" role="img" aria-label="Ornate filigree border"></div>
  <div class="abs ornament ornament--crest ornament--crest-top" role="img" aria-label="Decorative flourish"></div>
  <div class="abs hairline hairline--top"></div>
  <p class="abs centered couple">Derek and Leon</p>
  <div class="abs hairline hairline--bottom"></div>
  <div class="abs ornament ornament--crest ornament--crest-bottom" role="img" aria-label="Decorative flourish"></div>

  <p class="abs centered after-word">after</p>
  <p class="abs centered after-line">Derek and Leon’s Wedding: After Party</p>
  <div class="abs ornament ornament--divider" role="img" aria-label="Decorative scroll divider"></div>

  <p class="abs centered details">Saturday, May 23, 2015<br>7:30 PM<br>Harbor Crest Sailing Club<br>47 Pelling Road<br>San Francisco, CA</p>

  <div class="abs ornament ornament--border-bottom" role="img" aria-label="Ornate filigree border"></div>
</section>

</body>
</html>
```